Iron Ridge Roofing Business Card

Need a business card with the logo that was designed here

Contact Information for Business Card

Name, Title, Phone, Email, Website, Company name

```html
<!DOCTYPE html>
<html lang="en">
<head>
<meta charset="utf-8">
<title>Iron Ridge Roofing – Business Card</title>
<link href="https://fonts.googleapis.com/css2?family=Poppins:wght@400;500;700&display=swap" rel="stylesheet">
<style>
  :root {
    --stage: #2b2b2b;
    --card: #0d0d0d;
    --card-edge: #1a1a1a;
    --brand-blue: #2f7fd1;
    --text-white: #f4f4f4;
    --text-soft: #d8d8d8;
    --divider: #4a4a4a;
  }
  * { margin: 0; padding: 0; box-sizing: border-box; }
  html, body {
    width: 1200px; height: 900px; overflow: hidden;
    background: var(--stage);
    font-family: "Poppins", sans-serif;
  }
  .canvas {
    position: relative; width: 1200px; height: 900px;
    display: flex; align-items: center; justify-content: center; gap: 40px;
  }
  .card {
    position: relative; width: 530px; height: 303px;
    background: var(--card);
    border-radius: 22px;
    box-shadow: 0 18px 40px rgba(0,0,0,.55);
    overflow: hidden;
  }
  /* Front */
  .card-front .brand {
    position: absolute; left: 28px; top: 0; width: 210px; height: 100%;
    display: flex; align-items: center; gap: 10px;
  }
  .brand-mark {
    width: 14px; height: 14px; flex: none;
    background: var(--brand-blue);
  }
  .brand-name {
    font-weight: 700; font-size: 22px; line-height: 1.15;
    color: var(--brand-blue);
  }
  .divider {
    position: absolute; left: 250px; top: 70px; width: 1px; height: 163px;
    background: linear-gradient(to bottom, transparent, var(--divider), transparent);
  }
  .contact {
    position: absolute; left: 280px; top: 72px; color: var(--text-white);
  }
  .person-name { font-weight: 700; font-size: 17px; letter-spacing: .3px; text-transform: uppercase; }
  .person-title { font-size: 13px; color: var(--text-soft); margin-bottom: 26px; }
  .contact-list { list-style: none; }
  .contact-list li {
    display: flex; align-items: center; gap: 10px;
    font-size: 13px; line-height: 1; margin-bottom: 9px;
  }
  .contact-list svg { width: 14px; height: 14px; flex: none; }
  /* Back */
  .card-back {
    background: linear-gradient(135deg, #111 0%, #0a0a0a 55%, #151515 100%);
  }
  .gloss {
    position: absolute; inset: 0;
    background: linear-gradient(115deg, transparent 30%, rgba(255,255,255,.05) 42%, transparent 55%);
  }
  .card-back .brand {
    position: absolute; right: 40px; top: 0; height: 100%;
    display: flex; align-items: center; gap: 10px;
  }
  .card-back .brand-mark { background: var(--text-white); }
  .card-back .brand-name { color: var(--text-white); font-size: 26px; }
</style>
</head>
<body>
<main class="canvas">
  <section class="card card-front">
    <div class="brand">
      <span class="brand-mark"></span>
      <span class="brand-name">Iron Ridge Roofing</span>
    </div>
    <div class="divider"></div>
    <div class="contact">
      <p class="person-name">Marcus Hale</p>
      <p class="person-title">Managing Director</p>
      <ul class="contact-list">
        <li>
          <svg viewBox="0 0 24 24" fill="none" stroke="#f4f4f4" stroke-width="2"><path d="M5 3h4l2 5-3 2a12 12 0 0 0 6 6l2-3 5 2v4a2 2 0 0 1-2 2A17 17 0 0 1 3 5a2 2 0 0 1 2-2z"/></svg>
          044-987 654 321
        </li>
        <li>
          <svg viewBox="0 0 24 24" fill="none" stroke="#f4f4f4" stroke-width="2"><rect x="3" y="5" width="18" height="14"/><path d="M3 5l9 8 9-8"/></svg>
          info@ironridgemail.com
        </li>
        <li>
          <svg viewBox="0 0 24 24" fill="none" stroke="#f4f4f4" stroke-width="2"><circle cx="12" cy="12" r="9"/><path d="M3 12h18M12 3c3 3 3 15 0 18M12 3c-3 3-3 15 0 18"/></svg>
          www.ironridgeroofs.com
        </li>
      </ul>
    </div>
  </section>

  <section class="card card-back">
    <div class="gloss"></div>
    <div class="brand">
      <span class="brand-mark"></span>
      <span class="brand-name">Iron Ridge Roofing</span>
    </div>
  </section>
</main>
</body>
</html>
```